Paw Pantry

We need a word press template designed for our new Word press site.
We'd like to mimic the design of the old site somewhat:
http://www.pawpantry.example/
to be ported over to the new site:
http://www.pawpantry.example/wp
We like the ornamental dog bone style in the old sites's banner/navigation. We may want to mimic that somewhat in the new design.
We have a retail store in historic Harborton, NH and we bake gourmet dog teats and sell leashes, collars, outdoor gear, beds, soft-sided crates, interactive toys and premium dog & cat foods.
Retail

```html
<!DOCTYPE html>
<html lang="en">
<head>
<meta charset="utf-8">
<title>Paw Pantry – Gourmet Dog Treats</title>
<link href="https://fonts.googleapis.com/css2?family=PT+Sans:wght@400;700&family=Crimson+Text:wght@400;600&display=swap" rel="stylesheet">
<style>
:root{
  --green:#1f5e2f;
  --green-dark:#0c3a1a;
  --green-btn:#1d6a30;
  --orange:#c8461b;
  --orange-light:#e2581f;
  --gold:#dba418;
  --gold-dark:#a8700c;
  --ink:#2b2b2b;
  --body:#6b6b6b;
  --rule:#dddddd;
  --white:#ffffff;
}
*{margin:0;padding:0;box-sizing:border-box}
html,body{width:839px;height:1200px;overflow:hidden;background:var(--white)}
body{position:relative;font-family:"PT Sans",sans-serif;color:var(--body)}
.abs{position:absolute}
a{color:inherit;text-decoration:none}

/* header */
.header{left:0;top:0;width:839px;height:420px;background:linear-gradient(180deg,var(--green) 0%,#174f27 60%,var(--green-dark) 100%)}
.social{left:77px;top:46px;display:flex;gap:4px}
.social span{width:20px;height:20px;border-radius:50%;background:var(--white)}
.top-links{right:91px;top:15px;font-size:10px;color:var(--white);display:flex;align-items:center;gap:6px}
.top-links .sep{opacity:.8}
.order-btn{left:655px;top:46px;width:99px;height:25px;border-radius:3px;background:linear-gradient(var(--orange-light),var(--orange));color:var(--white);font-size:11px;display:flex;align-items:center;justify-content:center;gap:5px}
.ribbon{left:0;top:0}
.nav{top:82px;height:36px;display:flex;align-items:center;color:var(--white);font-size:13px}
.nav a{padding:0 12px;height:36px;line-height:36px;border-right:1px solid rgba(120,80,0,.35)}
.nav a:last-child{border-right:none}
.nav-left{left:89px}
.nav-right{left:498px}
.logo{left:365px;top:15px;width:110px;height:110px;border-radius:50%;background:#c42a1f;display:flex;align-items:center;justify-content:center;color:var(--white);font-weight:700;font-size:17px;box-shadow:0 0 0 4px var(--gold)}

/* slider */
.slider{left:59px;top:118px;width:721px;height:271px;background:var(--white);border-radius:0 0 6px 6px;box-shadow:0 2px 4px rgba(0,0,0,.3)}
.slide-title{left:51px;top:63px;font-size:29px;color:var(--orange);white-space:nowrap}
.slide-sub{left:51px;top:97px;font-size:19px;color:var(--green)}
.slide-text{left:53px;top:127px;width:290px;font-size:9.6px;line-height:16px}
.btn{display:inline-flex;align-items:center;justify-content:center;color:var(--white);border-radius:2px}
.btn-view{left:51px;top:168px;width:83px;height:24px;font-size:9.5px;background:linear-gradient(var(--orange-light),var(--orange))}
.slide-media{left:417px;top:6px;width:260px;height:256px;background:radial-gradient(ellipse at center,#d49a63 0%,#c98f5a 45%,#efe3d2 75%,var(--white) 100%)}
.dots{left:340px;top:244px;display:flex;gap:2px}
.dots span{width:8px;height:8px;border-radius:50%;background:#dcdcdc}
.dots span:first-child{background:#9a9a9a}

/* content */
.section-title{font-family:"Crimson Text",serif;font-size:17px;text-transform:uppercase;letter-spacing:.2px}
.welcome-title{left:60px;top:446px;color:var(--green)}
.frame{background:#f0f0f0;padding:6px;border-radius:3px}
.store-photo{left:60px;top:481px;width:123px;height:112px;border:1px solid #ddd;background:var(--white)}
.store-photo div{width:100%;height:100%;background:linear-gradient(180deg,#9a4a3a,#7b3a2e 55%,#5b4a44)}
.welcome-text{left:195px;top:480px;width:348px;font-size:9.6px;line-height:15.6px}
.welcome-text p+p{margin-top:6px}
.dotted{left:60px;top:623px;width:473px;border-top:1px dotted #bbb}
.products-title{left:60px;top:647px;color:var(--orange)}
.product-thumb{left:60px;width:146px;height:97px}
.product-thumb div{width:100%;height:100%}
.product-name{left:219px;font-size:14.5px;color:#3a3a3a}
.product-text{left:219px;width:320px;font-size:9.6px;line-height:15.6px}
.btn-cart{width:73px;height:20px;font-size:8px;background:linear-gradient(var(--orange-light),var(--orange))}
.btn-more{width:72px;height:20px;font-size:8px;background:linear-gradient(#2a8040,var(--green-btn))}
.row-rule{left:60px;width:480px;border-top:1px solid #e3e3e3}

/* sidebar */
.panel{left:563px;width:217px;border:1px solid var(--rule);background:var(--white)}
.why{top:439px;height:192px;background:linear-gradient(var(--white) 70%,#f2f2f2)}
.why h3{position:absolute;left:18px;top:14px;font-weight:400;font-size:18px;color:var(--green)}
.why .txt{position:absolute;left:18px;top:42px;width:186px;font-size:9.6px;line-height:15.6px}
.why .txt p+p{margin-top:6px}
.latest{top:643px;height:177px}
.latest-head{left:-1px;top:-1px;width:217px;height:35px;background:linear-gradient(var(--orange-light),#b83d15);color:var(--white);font-size:15px;padding:8px 15px}
.latest-photo{left:13px;top:45px;width:193px;height:118px;border:1px solid #e5e5e5;padding:4px;border-radius:3px}
.latest-photo div{width:100%;height:100%;background:linear-gradient(90deg,#b8a28a 0%,#a89076 45%,#7a5340 60%,#6b4535 100%)}
.social-box{top:830px;height:215px}
.page-thumb{left:16px;top:12px;width:58px;height:52px;border:1px solid #ddd;display:flex;align-items:center;justify-content:center}
.page-thumb span{width:36px;height:36px;border-radius:50%;background:#c42a1f}
.page-name{left:80px;top:12px;width:130px;font-size:11px;line-height:14px;color:#222}
.like-btn{left:80px;top:46px;width:38px;height:15px;border:1px solid #c8cfdf;background:#eef1f7;font-size:8px;color:#3b5a98;display:flex;align-items:center;justify-content:center;gap:2px}
.like-count{left:16px;top:71px;font-size:8.5px;color:#333}
.fans{left:16px;top:93px;display:grid;grid-template-columns:repeat(4,44px);gap:3px 2px}
.fans div{height:44px}
.plugin{left:16px;top:193px;font-size:8.5px;color:#333;display:flex;align-items:center;gap:4px}
.plugin span{width:11px;height:11px;background:#3b5a98}

/* footer */
.footer{left:0;top:1104px;width:839px;height:96px;background:linear-gradient(var(--green),var(--green-dark));border-top:1px dashed #3f8a55}
.footer-nav{left:60px;top:27px;font-size:10.5px;color:var(--white);display:flex;gap:5px}
.copyright{left:60px;top:49px;font-size:9px;color:#9bbca4}
.cards{left:654px;top:29px;display:flex;gap:3px}
.cards span{height:15px;background:var(--white);border-radius:1px}
</style>
</head>
<body>

<header class="header abs">
  <div class="social abs" aria-label="Social links"><span></span><span></span><span></span><span></span></div>

  <nav class="top-links abs">
    <a href="#">My Account</a><span class="sep">|</span>
    <a href="#">Wish List</a><span class="sep">|</span>
    <a href="#">Support</a><span class="sep">|</span>
    <a href="#">My Cart</a>
    <svg width="18" height="16" viewBox="0 0 18 16" aria-hidden="true"><path d="M1 2h3l2 8h9l2-6H5" fill="none" stroke="#fff" stroke-width="1.5"/><circle cx="7" cy="13.5" r="1.5" fill="#fff"/><circle cx="14" cy="13.5" r="1.5" fill="#fff"/></svg>
  </nav>

  <a class="order-btn abs" href="#">Online Order
    <svg width="14" height="14" viewBox="0 0 14 14" aria-hidden="true"><circle cx="7" cy="7" r="6.3" fill="none" stroke="#fff" stroke-width="1.3"/><path d="M4 7h6M7.5 4.5 10 7 7.5 9.5" fill="none" stroke="#fff" stroke-width="1.5"/></svg>
  </a>

  <svg class="ribbon abs" width="839" height="130" viewBox="0 0 839 130" aria-hidden="true">
    <polygon points="29,74 76,74 76,112 46,112 52,93" fill="var(--gold-dark)"/>
    <polygon points="810,74 763,74 763,112 793,112 787,93" fill="var(--gold-dark)"/>
    <rect x="59" y="82" width="721" height="36" fill="var(--gold)"/>
    <rect x="59" y="82" width="721" height="4" fill="#e8ba3a"/>
  </svg>

  <nav class="nav nav-left abs">
    <a href="#">HOME</a><a href="#">ABOUT</a><a href="#">NEWS</a><a href="#">EVENTS</a>
  </nav>
  <nav class="nav nav-right abs">
    <a href="#">OUR PRODUCTS</a><a href="#">OUR STORE</a><a href="#">CONTACT</a>
  </nav>

  <div class="logo abs">Paw Pantry</div>

  <section class="slider abs">
    <h1 class="slide-title abs" style="font-weight:400">Duis tincidunt lectus quis</h1>
    <h2 class="slide-sub abs" style="font-weight:400">Lorem ipsum dolor sit amet</h2>
    <p class="slide-text abs">Mauris neque metus, malesuada nec, ultricies sit amet, porttitor mattis, enim. In massa libero, interdum nec, interdum vel</p>
    <a class="btn btn-view abs" href="#">VIEW MORE</a>
    <div class="slide-media abs" role="img" aria-label="Four boxes of dog biscuits in red, green, blue and orange surrounded by small bone-shaped treats"></div>
    <div class="dots abs"><span></span><span></span><span></span><span></span></div>
  </section>
</header>

<main>
  <h2 class="section-title welcome-title abs" style="font-weight:400">Welcome to our website mainpage...</h2>
  <div class="store-photo frame abs"><div role="img" aria-label="Brick storefront of the shop with its sign above the door"></div></div>
  <div class="welcome-text abs">
    <p>Since 2004, Paw Pantry has been providing the Bayside with a unique shopping experience. In addition to our hand-made, all-natural dog treats we have significantly expanded our selection of leashes, collars, outdoor gear, beds, soft-sided crates, interactive toys and premium dog &amp; cat foods.</p>
    <p>We are conveniently located on Historic Market Street in the heart of the Harborton community. Whether you live in the Bayside or are visiting the area, stop on by, and make sure to bring your dog, they are always welcomed to help you shop.</p>
  </div>
  <div class="dotted abs"></div>

  <h2 class="section-title products-title abs" style="font-weight:400">Our Products</h2>

  <div class="product-thumb frame abs" style="top:677px"><div role="img" aria-label="Navy dog collar with a red lobster pattern" style="background:linear-gradient(180deg,#fff 15%,#1d2b55 15%,#1d2b55 85%,#fff 85%)"></div></div>
  <h3 class="product-name abs" style="top:674px;font-weight:400">Lobster Dog Collar</h3>
  <p class="product-text abs" style="top:697px">There is always something new in our bakery. Made fresh daily in small batches, Paw Pantry treats are made with the finest all-natural ingredients and are made to mimic yummy treats you’d find in a human bakery.</p>
  <a class="btn btn-cart abs" href="#" style="left:220px;top:750px">ADD TO CART</a>
  <a class="btn btn-more abs" href="#" style="left:298px;top:750px">READ MORE</a>
  <div class="row-rule abs" style="top:790px"></div>

  <div class="product-thumb frame abs" style="top:806px"><div role="img" aria-label="Three black bags of dog treats" style="background:linear-gradient(90deg,#fff 5%,#1a1a1a 5%,#1a1a1a 30%,#fff 30%,#fff 37%,#1a1a1a 37%,#1a1a1a 62%,#fff 62%,#fff 70%,#1a1a1a 70%,#1a1a1a 95%,#fff 95%)"></div></div>
  <h3 class="product-name abs" style="top:803px;font-weight:400">Product Tittl here</h3>
  <p class="product-text abs" style="top:826px">There is always something new in our bakery. Made fresh daily in small batches, Paw Pantry treats are made with the finest all-natural ingredients and are made to mimic yummy treats you’d find in a human bakery.</p>
  <a class="btn btn-cart abs" href="#" style="left:220px;top:879px">ADD TO CART</a>
  <a class="btn btn-more abs" href="#" style="left:298px;top:879px">READ MORE</a>
  <div class="row-rule abs" style="top:922px"></div>

  <div class="product-thumb frame abs" style="top:938px"><div role="img" aria-label="Clear bags of golden sweet potato chews" style="background:radial-gradient(ellipse at center,#d9a447 0%,#e8c27a 45%,#fff 80%)"></div></div>
  <h3 class="product-name abs" style="top:935px;font-weight:400">Product Tittl here</h3>
  <p class="product-text abs" style="top:958px">There is always something new in our bakery. Made fresh daily in small batches, Paw Pantry treats are made with the finest all-natural ingredients and are made to mimic yummy treats you’d find in a human bakery.</p>
  <a class="btn btn-cart abs" href="#" style="left:220px;top:1010px">ADD TO CART</a>
  <a class="btn btn-more abs" href="#" style="left:298px;top:1010px">READ MORE</a>
</main>

<aside>
  <section class="panel why abs">
    <h3>Why Choose Us</h3>
    <div class="txt">
      <p>Mauris vel lacus vitae felis vestibulum volutpat. Etiam est nunc, venenatis in, tristique eu, imperdiet ac, nisl.</p>
      <p>Cum sociis natoque penatibus et magnis dis parturient montes, nascetur ridiculus mus. In iaculis facilisis massa. Etiam eu urna. Sed porta. Suspendisse quam leo, molestie sed, luctus quis, feugiat in, pede.</p>
    </div>
  </section>

  <section class="panel latest abs">
    <h3 class="latest-head abs" style="font-weight:400">Latest Photo</h3>
    <div class="latest-photo abs"><div role="img" aria-label="Tray of round biscuits and chocolate heart-shaped dog treats"></div></div>
  </section>

  <section class="panel social-box abs">
    <div class="page-thumb abs"><span></span></div>
    <div class="page-name abs">Paw Pantry Gourmet Dog Bakery</div>
    <div class="like-btn abs">Like</div>
    <div class="like-count abs">155 people like Paw Pantry Gourmet</div>
    <div class="fans abs" role="img" aria-label="Grid of eight fan profile photos">
      <div style="background:#8aa0b5"></div><div style="background:#a0707a"></div><div style="background:#d9b4a0"></div><div style="background:#b07a55"></div>
      <div style="background:#c29a88"></div><div style="background:#9a9a9a"></div><div style="background:#5a4a50"></div><div style="background:#a88570"></div>
    </div>
    <div class="plugin abs"><span></span>Friendbook social plugin</div>
  </section>
</aside>

<footer class="footer abs">
  <nav class="footer-nav abs">
    <a href="#">HOME</a>|<a href="#">ABOUT</a>|<a href="#">SERVICE</a>|<a href="#">CLIENTS</a>|<a href="#">EVENT</a>|<a href="#">RESOURCE</a>|<a href="#">HOW IT WORKS</a>|<a href="#">BLOG</a>|<a href="#">CONTACT US</a>
  </nav>
  <p class="copyright abs">© 2013 Company Name.&nbsp; All right reserved.&nbsp; Term of Use</p>
  <div class="cards abs" aria-label="Accepted payment methods"><span style="width:24px"></span><span style="width:24px"></span><span style="width:24px"></span><span style="width:39px"></span></div>
</footer>

</body>
</html>
```